company anniversary card

Create a single-sided postcard
Background: Yellow
Message: “88 Jahre FLENDAAAAK! Danke für die tOOOOle Zusammenarbeit.”
The three different logos can be used, as well as the old photo.
I’m open to further suggestions — you can find more ideas at www.flendaaaak.ch.

```html
<!DOCTYPE html>
<html lang="de">
<head>
<meta charset="utf-8">
<title>FLENDAAAAK – 88 Jahre Jubiläumskarte</title>
<link rel="stylesheet" href="https://fonts.googleapis.com/css2?family=Fredoka:wght@500;600;700&family=Lexend:wght@400;600&display=swap">
<style>
  :root {
    --stage: #151515;
    --card-yellow: #fcd91c;
    --ink: #0b0b0b;
    --paper: #ffffff;
    --muted-olive: #a8941f;
    --photo-light: #cbbfa6;
    --photo-dark: #6d624f;
  }
  * { margin: 0; padding: 0; box-sizing: border-box; }
  html, body {
    width: 1200px; height: 1200px; overflow: hidden;
    background: var(--stage);
  }
  .stage {
    position: relative; width: 1200px; height: 1200px;
  }
  .postcard {
    position: absolute; left: 170px; top: 0;
    width: 860px; height: 1200px;
    border-radius: 37px;
    background: var(--card-yellow);
    overflow: hidden;
  }
  .postcard svg { display: block; }
  .wordmark { font-family: "Fredoka", sans-serif; font-weight: 700; fill: var(--ink); }
  .tagline { font-family: "Lexend", sans-serif; font-weight: 400; fill: var(--ink); letter-spacing: 3.4px; }
  .age-digits { font-family: "Fredoka", sans-serif; font-weight: 700; fill: var(--paper); stroke: var(--ink); stroke-width: 5; paint-order: stroke; }
  .age-label { font-family: "Fredoka", sans-serif; font-weight: 700; fill: var(--ink); stroke: var(--card-yellow); stroke-width: 5; paint-order: stroke; }
  .thanks { font-family: "Fredoka", sans-serif; font-weight: 600; fill: var(--ink); }
  .jubilee-mark { font-family: "Fredoka", sans-serif; font-weight: 700; fill: var(--muted-olive); }
  .website { font-family: "Lexend", sans-serif; font-weight: 600; fill: var(--ink); letter-spacing: 9px; }
</style>
</head>
<body>
<main class="stage">
  <article class="postcard">
    <svg width="860" height="1200" viewBox="0 0 860 1200" xmlns="http://www.w3.org/2000/svg">
      <defs>
        <linearGradient id="archive-tone" x1="0" y1="0" x2="0" y2="1">
          <stop offset="0" stop-color="var(--photo-light)"/>
          <stop offset="0.6" stop-color="var(--photo-dark)"/>
          <stop offset="1" stop-color="var(--photo-light)"/>
        </linearGradient>
      </defs>

      <!-- header brand -->
      <g class="brand-header">
        <text class="wordmark" x="430" y="136" font-size="56" text-anchor="middle" textLength="388" lengthAdjust="spacingAndGlyphs">FLENDAAAAK</text>
        <text class="tagline" x="430" y="168" font-size="17" text-anchor="middle" textLength="388" lengthAdjust="spacing">HAUSTECHNIK + BAUSPENGLEREI</text>
      </g>

      <!-- bracket frame -->
      <path class="frame" d="M117 265 H100 A20 20 0 0 0 80 285 V912 A37 37 0 0 0 117 949 H177 M702 949 H741 A37 37 0 0 0 778 912 V285 A20 20 0 0 0 758 265 H745"
            fill="none" stroke="var(--ink)" stroke-width="3"/>

      <!-- archive photo area -->
      <rect class="archive-photo" x="84" y="470" width="692" height="174" fill="url(#archive-tone)"
            role="img" aria-label="Altes Schwarzweissfoto: eine Reihe Lieferwagen mit 24-Stunden-Service-Beschriftung vor einer Altstadt mit Wasserturm"/>

      <!-- anniversary number -->
      <text class="age-digits" x="441" y="493" font-size="372" text-anchor="middle" textLength="460" lengthAdjust="spacingAndGlyphs">88</text>
      <text class="age-label" x="433" y="386" font-size="50" text-anchor="middle" textLength="168" lengthAdjust="spacingAndGlyphs">JAHRE</text>

      <!-- main brand -->
      <text class="wordmark" x="428" y="739" font-size="84" text-anchor="middle" textLength="563" lengthAdjust="spacingAndGlyphs">FLENDAAAAK</text>

      <!-- message -->
      <g class="thanks">
        <text x="437" y="814" font-size="62" text-anchor="middle">Danke für die</text>
        <text x="437" y="881" font-size="62" text-anchor="middle">tOOOOle</text>
        <text x="437" y="947" font-size="62" text-anchor="middle" textLength="478" lengthAdjust="spacingAndGlyphs">Zusammenarbeit</text>
      </g>

      <!-- jubilee marks -->
      <g class="jubilee-mark">
        <text x="162" y="1078" font-size="50" textLength="268" lengthAdjust="spacingAndGlyphs">88 JAHRE</text>
        <text x="470" y="1074" font-size="50" textLength="250" lengthAdjust="spacingAndGlyphs">FLENDAAAAK</text>
      </g>

      <!-- website -->
      <text class="website" x="428" y="1142" font-size="15" text-anchor="middle">www.flendaaaak.ch</text>
    </svg>
  </article>
</main>
</body>
</html>
```